lawn sign

we need a design for our organic mosquito spray service. should fit a 27in x 18in yard sign. Includes our company logo and a picture of a mosquito with a circle around it crossed out (example included).

It needs to be simple, easily readable and in clear resolution. Signs needs to include the text: "this lawn receives ORGANIC treatments for mosquitoes and chiggers. Instantly SAFE for people and pets".

Include our phone number and website "615-372-5160" "yardnestle.com"

our ideas are: organic = no pests (use example pic)
no chemicals used = safe
Updates

Project Deadline Extended
Reason: we have been too busy to look at all of the designs. we will look at them all in the next day. thank you for your efforts and creativity!

Industry/Entity Type

It Company

```html
<!DOCTYPE html>
<html lang="en">
<head>
<meta charset="utf-8">
<title>Yard Nestle – Organic Mosquito Treatment Lawn Sign</title>
<link rel="stylesheet" href="https://fonts.googleapis.com/css2?family=Questrial&family=Montserrat:wght@600&display=swap">
<style>
  :root {
    --sign-bg: #ffffff;
    --alert-red: #ec1c24;
    --organic-green: #8dc63f;
    --safe-blue: #3b8fd0;
    --insect-grey: #8c8c8c;
  }
  html, body {
    margin: 0;
    padding: 0;
    overflow: hidden;
    background: var(--sign-bg);
  }
  .sign {
    position: relative;
    width: 800px;
    height: 1200px;
    overflow: hidden;
    background: var(--sign-bg);
    font-family: "Questrial", "Century Gothic", sans-serif;
    text-align: center;
  }
  .no-pest-symbol {
    position: absolute;
    left: 200px;
    top: 21px;
    width: 400px;
    height: 400px;
  }
  .line {
    position: absolute;
    left: 0;
    width: 100%;
    margin: 0;
    line-height: 1;
    white-space: nowrap;
  }
  .line--red { color: var(--alert-red); font-size: 54px; }
  .line--organic {
    color: var(--organic-green);
    font-size: 84px;
    letter-spacing: 12px;
    padding-left: 12px;
  }
  .line--blue { color: var(--safe-blue); font-size: 52px; }
  .safe-word { font-size: 72px; letter-spacing: 6px; }
  .brand-name {
    color: var(--safe-blue);
    font-size: 60px;
  }
  .phone {
    color: var(--safe-blue);
    font-family: "Montserrat", "Arial", sans-serif;
    font-weight: 600;
    font-size: 46px;
    letter-spacing: 5px;
  }
</style>
</head>
<body>
<main class="sign">
  <svg class="no-pest-symbol" viewBox="0 0 400 400" aria-hidden="false">
    <g role="img" aria-label="Grey mosquito illustration">
      <ellipse cx="215" cy="190" rx="130" ry="95" fill="var(--insect-grey)" opacity="0.85"/>
    </g>
    <circle cx="200" cy="200" r="172" fill="none" stroke="var(--alert-red)" stroke-width="32"/>
    <line x1="78" y1="78" x2="322" y2="322" stroke="var(--alert-red)" stroke-width="32"/>
  </svg>

  <p class="line line--red" style="top:459px">this lawn receives</p>
  <p class="line line--organic" style="top:522px">ORGANIC</p>
  <p class="line line--red" style="top:610px">treatment for</p>
  <p class="line line--red" style="top:674px">mosquitoes and</p>
  <p class="line line--red" style="top:741px">chiggers</p>
  <p class="line line--blue" style="top:827px">instantly <span class="safe-word">SAFE</span> for</p>
  <p class="line line--blue" style="top:912px">people and pets</p>

  <p class="line brand-name" style="top:1020px">yardnestle.com</p>
  <p class="line phone" style="top:1087px">615-372-5160</p>
</main>
</body>
</html>
```